この度は、たくさんのご提案をいただきまして、
誠にありがとうございました。
多くの素晴らしいデザインをご提案していただき、
本当に感謝しております。
今回、ご選考の結果、
ruto_artsさんのデザインを採用させていただきました。
※本案件に関しましては、書籍のイメージに一番合ったものが、
ruto_artsさんの表紙デザインだったため、
今回は、ruto_artsさんのご提案を選定させていただきました。
本当に、ありがとうございました。
また、今回は残念ながら、ご採用に至らなかった方も、
この度はお忙しいところ、本案件にご参加いただきまして、
今後も、継続的にお仕事をご発注させていただきますので、
また宜しければご参加いただければ幸いです。
以上、今後とも、何卒よろしくお願いいたします。
仕事は丁寧に進めていきたいと考えております。
もし、わからない点などがあれば、遠慮なく仰ってください。
1回切りのお仕事だけでなく、継続的にお仕事ができる方を探しております。

```html
<!DOCTYPE html>
<html lang="ja">
<head>
<meta charset="utf-8">
<title>普通の主婦の実体験記のすべて!</title>
<link href="https://fonts.googleapis.com/css2?family=M+PLUS+Rounded+1c:wght@500;800;900&display=swap" rel="stylesheet">
<style>
  :root {
    --yellow: #ffe000;
    --sky: #3b9fe0;
    --red: #e60012;
    --brown: #8a5a2e;
    --green: #4cae32;
    --ink: #333333;
    --white: #ffffff;
    --door-tone: #eceae6;
    --woman-tone: #f6d9c8;
  }
  html, body { margin: 0; padding: 0; overflow: hidden; }
  body { width: 749px; height: 1200px; background: var(--white); }
  .cover {
    position: relative; width: 749px; height: 1200px; overflow: hidden;
    font-family: "M PLUS Rounded 1c", sans-serif;
    background: var(--white);
  }
  .band-top { position: absolute; left: 0; top: 0; width: 749px; height: 290px; background: var(--yellow); }
  .band-sky { position: absolute; left: 0; top: 290px; width: 749px; height: 230px; background: var(--sky); }
  .band-blurb { position: absolute; left: 0; top: 960px; width: 749px; height: 240px; background: var(--sky); }

  .title {
    position: absolute; left: 0; top: 12px; width: 749px; margin: 0;
    text-align: center; font-weight: 900; font-size: 94px; line-height: 94px;
    color: var(--red); letter-spacing: 2px;
    -webkit-text-stroke: 16px var(--white); paint-order: stroke fill;
  }
  .zero { position: absolute; left: 260px; top: 290px; }
  .yen {
    position: absolute; left: 0; top: 575px; width: 749px; text-align: center;
    font-weight: 900; font-size: 76px; color: var(--red); line-height: 1;
  }
  .bubble {
    position: absolute; width: 196px; height: 196px; border-radius: 50%;
    display: flex; align-items: center; justify-content: center; text-align: center;
    color: var(--white); font-weight: 800; font-size: 42px; line-height: 1.2;
    border: 5px solid var(--white); box-sizing: border-box;
  }
  .bubble--constipation { left: 80px; top: 447px; background: var(--brown); }
  .bubble--pollen { left: 470px; top: 447px; background: var(--green); }

  .art { position: absolute; }
  .art--door { left: 130px; top: 640px; width: 170px; height: 290px; background: linear-gradient(180deg, var(--door-tone), #d8d5cf); }
  .art--woman { left: 495px; top: 690px; width: 215px; height: 215px; background: radial-gradient(circle at 50% 45%, var(--woman-tone), #f3c6cf); border-radius: 40%; }

  .author { position: absolute; left: 320px; top: 800px; width: 140px; text-align: center; color: var(--ink); }
  .author-mark {
    width: 44px; height: 44px; border-radius: 50%; background: var(--red); color: var(--white);
    margin: 0 auto 6px; display: flex; align-items: center; justify-content: center;
    font-weight: 800; font-size: 24px;
  }
  .author-name { font-weight: 800; font-size: 32px; line-height: 1.15; }

  .blurb {
    position: absolute; left: 30px; top: 985px; width: 690px; margin: 0;
    color: var(--white); font-weight: 500; font-size: 24px; line-height: 1.6;
    text-align: justify;
  }
</style>
</head>
<body>
<div class="cover">
  <div class="band-top"></div>
  <div class="band-sky"></div>

  <h1 class="title">普通の主婦の<br>実体験記の<br>すべて!</h1>

  <svg class="zero" width="240" height="285" viewBox="0 0 240 285" aria-label="0">
    <ellipse cx="120" cy="142" rx="112" ry="135" fill="var(--white)"/>
    <ellipse cx="120" cy="142" rx="88" ry="112" fill="none" stroke="var(--red)" stroke-width="52"/>
  </svg>
  <div class="yen">円で</div>

  <div class="bubble bubble--constipation">便秘よ<br>さらば</div>
  <div class="bubble bubble--pollen">さよなら<br>花粉症</div>

  <div class="art art--door" role="img" aria-label="トイレのドアの前で喜ぶ女性のイラスト"></div>
  <div class="art art--woman" role="img" aria-label="花粉症が治り笑顔でティッシュを持つ女性のイラスト"></div>

  <div class="author">
    <div class="author-mark">著</div>
    <div class="author-name">オフィス<br>桜井</div>
  </div>

  <div class="band-blurb"></div>
  <p class="blurb">長年悩まされた便秘と花粉症を普通の主婦が、誰の助けも得ず、毎日の生活を変えることなく、ついにどちらの悩みも解決させました。しかも0円で。医療関係者ではないふつうの主婦の実体験です。今では便秘よさらばで快適な日々。あんなにつらかった花粉症の症状さえもう思い出せません。</p>
</div>
</body>
</html>
```